依頼詳細
2021年11月25日から28日まで下落合のRUMBA2046で行います。

7・Marelle×FoldedMothS合併公演

題名
「灯影ノ箱」(そらごとのいろ)※ノはカタカナです。

あらすじ
彩は幸せだった。慎ましい暮らしだが、彩が幼い頃から思い焦がれていた、普通の幸せだ。
長屋の者は皆親切で、夫の玄之助は誰よりも優しい人だ。だから玄之助が友人の借金を背負ってしまった時も咎めなかった。むしろこの人らしいと、好ましくさえ思えた。
とはいえ金は返さなくてはいけない。幸い、彩は手に職があった。この時ばかりは、技術を仕込んでくれた父に感謝した。

また人を殺すのは気が重いが、この幸せを守るためなら。

こちらの公演のチラシデザインをお願いしたいです。
タイトルロゴは、可能であれば既存のフォントをそのまま使用するのではなくデザインしていただけるとありがたいです。
裏面は、情報量が多く、現時点で未確定な情報もありますので、デザイナーさんを絞ってから直接連絡させていただきます。
表面のデザインはチケット等にも使用したいと考えておりますので、タイトルロゴや文字情報とデザインを別々のデータでいただけると助かります。

表面カラー(CMYK)、裏面白黒2色です。
裏面は文字情報が多く載ります。
出演者が23人になる予定です、各出演者の写真も利用して頂きたいと考えております。

過去公演の参考です。
http://7marelle-example.com/tate/wp-content/uploads/vol11/夕霞.pdf
記載項目
タイトル 灯影ノ箱

他情報
7・Marelle×FoldedMothS合併記念公演第2弾
2021年11月25日(木)〜28日(日)
会場 下落合RUMBA2046

劇団ロゴ(添付ファイル)
サイズ
A4
ページ数
両面
希望イメージ
シンプル 複雑
単色 カラフル
暗い 明るい
日常 高級
遊び心 厳粛
未来的 伝統的
女性的 男性的
希望する色
黄・オレンジ系、青系、紫系、登場人物が色に因んた名前です、鮮やかだけどどこか寂しげな
納品ファイル
• イラストレーター形式 (.ai)
補足説明
イラストレーターのバージョンはCS2でお願いします。
メインの舞台は丘上の大きな屋敷になります。
物語のテーマとして、人の二面性、表の顔と裏の顔、嘘と真実などがあり、それを紅葉の色の変化と紐付けて表現するよていです。
上記、必ず描いて欲しいものではありませんが、イメージの参考になりましたら。
参考用の添付ファイルには画像を使用してますが今回画像は使用しない方向で考えております。

今回の公演のイメージにピッタリだったので選ばせて頂きました!

皆様素敵なデザインをありがとうございました。
とても嬉しく感謝しておりますm(_ _)m

```html
<!DOCTYPE html>
<html lang="ja">
<head>
<meta charset="utf-8">
<title>灯影ノ箱 — 7・Marelle×FoldedMothS 合併記念公演第２弾</title>
<link rel="stylesheet" href="https://fonts.googleapis.com/css2?family=Shippori+Mincho+B1:wght@500;700&family=Noto+Sans+JP:wght@400;500;700&display=swap">
<style>
  :root {
    --ink-white: #ffffff;
    --tone-charcoal: #2c2c30;
    --tone-slate: #4a4a52;
    --tone-yellow: #f2c21a;
    --tone-orange: #e8881c;
    --tone-teal: #1f8f8a;
    --tone-blue: #1f4fb0;
    --tone-violet: #3a2a9a;
    --tone-purple: #5a3fb8;
    --tone-lavender: #b7b4e0;
  }
  html, body {
    margin: 0;
    padding: 0;
    overflow: hidden;
    background: #ffffff;
  }
  .flyer {
    position: relative;
    width: 847px;
    height: 1200px;
    overflow: hidden;
    color: var(--ink-white);
    font-family: "Noto Sans JP", sans-serif;
  }
  .flyer__artwork {
    position: absolute;
    inset: 0;
    background: linear-gradient(100deg,
      var(--tone-charcoal) 0%,
      var(--tone-slate) 22%,
      var(--tone-yellow) 34%,
      var(--tone-orange) 44%,
      var(--tone-teal) 54%,
      var(--tone-blue) 64%,
      var(--tone-violet) 74%,
      var(--tone-purple) 84%,
      var(--tone-lavender) 100%);
  }
  .flyer__series {
    position: absolute;
    top: 22px;
    left: 0;
    width: 100%;
    text-align: center;
    font-size: 21px;
    font-weight: 500;
    letter-spacing: 0.04em;
  }
  .flyer__ring {
    position: absolute;
    left: 297px;
    top: 300px;
    width: 254px;
    height: 254px;
  }
  .flyer__title {
    position: absolute;
    top: 118px;
    left: 50%;
    transform: translateX(-50%);
    margin: 0;
    writing-mode: vertical-rl;
    font-family: "Shippori Mincho B1", serif;
    font-weight: 700;
    font-size: 132px;
    line-height: 1;
    letter-spacing: 0.02em;
  }
  .flyer__schedule {
    position: absolute;
    top: 690px;
    left: 0;
    width: 100%;
    text-align: center;
  }
  .schedule__year {
    display: block;
    font-size: 34px;
    font-weight: 500;
    line-height: 1;
    margin-left: -130px;
  }
  .schedule__dates {
    display: block;
    font-size: 74px;
    font-weight: 500;
    line-height: 1.05;
    letter-spacing: 0.01em;
  }
  .schedule__day {
    display: inline-block;
    width: 30px;
    height: 30px;
    line-height: 30px;
    border-radius: 50%;
    background: var(--ink-white);
    color: var(--tone-blue);
    font-size: 18px;
    font-weight: 700;
    vertical-align: 8px;
    margin: 0 4px;
  }
  .schedule__arrow {
    font-size: 44px;
    vertical-align: 12px;
  }
  .schedule__venue {
    display: block;
    margin-top: 6px;
    font-size: 30px;
    font-weight: 700;
    letter-spacing: 0.02em;
  }
  .flyer__company {
    position: absolute;
    left: 0;
    top: 1062px;
    width: 100%;
    display: flex;
    justify-content: center;
    align-items: center;
    gap: 10px;
    font-size: 24px;
    font-weight: 500;
  }
  .company__mark {
    width: 18px;
    height: 18px;
    border-radius: 50%;
    background: var(--ink-white);
  }
</style>
</head>
<body>
<main class="flyer">
  <div class="flyer__artwork" role="img" aria-label="Layered strips of dyed fabric in charcoal, yellow, orange, teal, blue with autumn leaf pattern, purple and lavender"></div>

  <p class="flyer__series">7・Marelle×FoldedMothS 合併記念公演第２弾</p>

  <svg class="flyer__ring" viewBox="0 0 254 254" aria-hidden="true">
    <circle cx="127" cy="127" r="125" fill="none" stroke="var(--ink-white)" stroke-width="1.6"/>
  </svg>

  <h1 class="flyer__title">灯影ノ箱</h1>

  <div class="flyer__schedule">
    <span class="schedule__year">2021</span>
    <span class="schedule__dates">11.25<span class="schedule__day">木</span><span class="schedule__arrow">▶</span>28<span class="schedule__day">日</span></span>
    <span class="schedule__venue">会場：下落合RUMBA2046</span>
  </div>

  <div class="flyer__company">
    <span class="company__mark"></span>
    <span class="company__name">FoldedMothS</span>
  </div>
</main>
</body>
</html>
```